Crest of Morning Paddocks Business Cards with logo

Need a creative business card that pops. Colorful but professional. The attached logo should be included. We are a national horse racing partnership so we are in the equine business. Nothing cartoonlike or whimsical.

Target Market(s)

professionals - 40+

Contact Information for Business Card

Maren Dunleavy
Director of Operations
27 Ashbrook Lane
Middletown, MD. 21584

Phone (313) 555-0147

FX: (949) 555-0192

email: maren@cmpaddocks.example
cmpaddocks.example

Requirements
Must have
• All information above should be on the business card including the website address. Professional yet creative
Nice to have
• an attention grabbing design. not boring. exciting.
Should not have
• cartoon like - whimsical.

```html
<!DOCTYPE html>
<html lang="en">
<head>
<meta charset="utf-8">
<title>Crest of Morning Paddocks – Business Card</title>
<link href="https://fonts.googleapis.com/css2?family=Arimo:wght@400;700&display=swap" rel="stylesheet">
<style>
  :root {
    --royal: #333f9c;
    --royal-deep: #27328a;
    --gold: #cdb434;
    --paper: #ffffff;
    --ink: #2f3a92;
    --backdrop: #e9e7e2;
  }
  html, body {
    margin: 0;
    width: 1200px;
    height: 780px;
    overflow: hidden;
    background: var(--backdrop);
    font-family: "Arimo", Arial, sans-serif;
  }
  .card {
    position: absolute;
    left: 100px;
    top: 100px;
    width: 1000px;
    height: 580px;
    border-radius: 36px;
    overflow: hidden;
    background: var(--paper);
    box-shadow: 0 10px 30px rgba(0,0,0,0.18);
  }
  .card-art { position: absolute; inset: 0; }
  .identity {
    position: absolute;
    right: 48px;
    top: 30px;
    text-align right;
    text-align: right;
    color: var(--paper);
  }
  .identity-name { margin: 0; font-size: 36px; font-weight: 700; letter-spacing: 0.3px; }
  .identity-title { margin: 4px 0 0; font-size: 21px; font-weight: 400; }
  .brand {
    position: absolute;
    left: 340px;
    top: 360px;
    display: flex;
    align-items: center;
    gap: 14px;
  }
  .brand-dot {
    width: 26px; height: 26px; border-radius: 50%;
    background: var(--gold);
    flex: none;
  }
  .brand-name {
    font-size: 26px;
    font-weight: 700;
    color: var(--ink);
    white-space: nowrap;
  }
  .contact-row {
    position: absolute;
    left: 230px;
    right: 40px;
    top: 440px;
    border-top: 2px solid var(--gold);
    padding-top: 20px;
    display: flex;
    justify-content: space-between;
    color: var(--ink);
    font-size: 19px;
  }
  .contact-group {
    padding: 0 0 0 22px;
    border-left: 2px solid var(--gold);
  }
  .contact-group:first-child { border-left: none; padding-left: 0; }
  .contact-line { display: flex; align-items: center; gap: 9px; margin: 0 0 8px; white-space: nowrap; }
  .contact-icon { width: 17px; height: 17px; flex: none; }
  .address-line { margin: 0 0 8px; white-space: nowrap; }
</style>
</head>
<body>
  <div class="card">
    <svg class="card-art" viewBox="0 0 1000 580" width="1000" height="580" aria-hidden="true">
      <defs>
        <linearGradient id="royalBand" x1="0" y1="0" x2="1" y2="1">
          <stop offset="0" stop-color="#3a47a6"/>
          <stop offset="1" stop-color="#27328a"/>
        </linearGradient>
      </defs>
      <rect width="1000" height="580" fill="url(#royalBand)"/>
      <path d="M1000,130 C700,130 250,230 60,580 L1000,580 Z" fill="#ffffff"/>
      <path d="M1000,150 C710,152 280,252 96,580" fill="none" stroke="#cdb434" stroke-width="8"/>
    </svg>

    <div class="identity">
      <p class="identity-name">Maren Dunleavy</p>
      <p class="identity-title">Director of Operations</p>
    </div>

    <div class="brand">
      <span class="brand-dot"></span>
      <span class="brand-name">Crest of Morning Paddocks</span>
    </div>

    <div class="contact-row">
      <div class="contact-group">
        <p class="contact-line">
          <svg class="contact-icon" viewBox="0 0 24 24"><path d="M6 2h4l2 5-3 2a12 12 0 0 0 6 6l2-3 5 2v4c0 1-1 2-2 2A18 18 0 0 1 4 4c0-1 1-2 2-2z" fill="#cdb434"/></svg>
          (313) 555-0147
        </p>
        <p class="contact-line">
          <svg class="contact-icon" viewBox="0 0 24 24"><rect x="6" y="2" width="12" height="7" fill="#cdb434"/><rect x="2" y="10" width="20" height="9" rx="2" fill="#cdb434"/><rect x="6" y="15" width="12" height="7" fill="#fff" stroke="#cdb434" stroke-width="2"/></svg>
          (949) 555-0192
        </p>
      </div>
      <div class="contact-group">
        <p class="contact-line">
          <svg class="contact-icon" viewBox="0 0 24 24"><rect x="2" y="5" width="20" height="14" fill="#cdb434"/><path d="M2 5l10 8 10-8" fill="none" stroke="#fff" stroke-width="2"/></svg>
          maren@cmpaddocks.example
        </p>
        <p class="contact-line">
          <svg class="contact-icon" viewBox="0 0 24 24"><circle cx="12" cy="12" r="10" fill="#cdb434"/><path d="M2 12h20M12 2c-4 5-4 15 0 20M12 2c4 5 4 15 0 20" fill="none" stroke="#fff" stroke-width="1.5"/></svg>
          cmpaddocks.example
        </p>
      </div>
      <div class="contact-group">
        <p class="address-line">27 Ashbrook Lane</p>
        <p class="address-line">Middletown, MD. 21584</p>
      </div>
    </div>
  </div>
</body>
</html>
```